TALVENTO needs a Sleek, Professional and Serious Web Design, this web design is aiming to be famous!

Dear Designers,

We need a web design for a new company based on the Internet named "talvento". I have already worked with PX to get my logo and it has been a wonderful experience which I want to repeat. We are kind of work social network, the web page will be mostly used to write comments on businesses around the world to help workers find which company fit the best for them. This website is also here to help people finding work by giving them the tools to make the right research.

For contents inspiration, you could see on the added files a sketch of the website but I am not asking you following it because it was just for giving the contents.

We do not have any example regarding website that we do like because all are coming so generic. We would like a very sleek website, where surfing become very intuitive and ergonomic (Brindlepost is not very ergonomic for example from our point of view). The website must reflect professionalism and seriousness and worker, world connexion.

We will be pleased to accept original designs as long as they fit to our requirements and if it is properly made of course: e.g. web page looking like a newspaper etc.

About colours, we are not decided yet but we are aiming a light orange (pastel style) or dark bluish green. Also, it comes to our attention that a web site mostly realized in grey-scale will be very interesting (touch of colour will be accepted as well if it miss too much dynamism) .

We will give the feedback as soon as possible because we would like to have 5 pages but it will be only very small changes on the next ones. (like adding 4 buttons)

Target Market(s)

Our target is relatively large because it is all people of working age, in numbers we can say a range of people aged from 18 to 45 years.

Industry/Entity Type

Internet

Number of Pages Required

3 page

Font styles to use
Sans Serif

Requirements
Must have
• Elements that must be on the web page are exposed below:
• - company logo ( .ai & .eps files on added files)
• - 4 buttons (Searcher "highlighted" / Advises / Jobs / Solutions)
• - login/account window
• - language button (e.g. a flag)
• - Window companies searcher (the most important, refer to the sketch)
• - classic menu down the page - about us / contact us / conditions / site map / community / politics / publicity / languages / copyright etc.
Nice to have
• We want a professional and serious website.
Should not have
• If you have a doubt, just ask us because nothing are coming to our mind.

```html
<!DOCTYPE html>
<html lang="en">
<head>
<meta charset="utf-8">
<title>Talvento</title>
<link rel="stylesheet" href="https://fonts.googleapis.com/css2?family=Oswald:wght@500;600&family=Roboto+Condensed:wght@300;400;700&display=swap">
<style>
:root{
  --green:#3ebd96;
  --green-dark:#2fa37f;
  --green-pale:#e3efeb;
  --charcoal:#3c3c3c;
  --charcoal-2:#4a4a4a;
  --slate:#5e6b7a;
  --slate-dark:#525e6c;
  --grey-band:#e7e7e7;
  --grey-panel:#d6d9dd;
  --ink:#3a3a3a;
  --muted:#6b6b6b;
  --white:#fff;
}
*{box-sizing:border-box;margin:0;padding:0}
html,body{width:814px;height:1200px;overflow:hidden}
body{position:relative;background:#f3f3f3;font-family:"Roboto Condensed",Arial,sans-serif;color:var(--ink)}
.abs{position:absolute}
/* header */
.topbar{left:0;top:0;width:814px;height:37px;background:var(--charcoal)}
.brand{left:0;top:0;width:269px;height:37px;background:var(--green)}
.brand-name{left:170px;top:8px;font-family:"Roboto Condensed",sans-serif;font-weight:700;font-size:19px;color:var(--charcoal);letter-spacing:.3px;display:flex;align-items:center;gap:4px}
.brand-name i{display:block;width:9px;height:9px;border-radius:50%;background:var(--charcoal)}
.util-btn{top:11px;height:16px;font-size:6px;text-transform:uppercase;display:flex;align-items:center;justify-content:center;gap:4px;box-shadow:0 2px 0 rgba(0,0,0,.25)}
.util-lang{left:466px;width:52px;background:#e9e9e9;color:#444}
.util-login{left:534px;width:44px;background:var(--green);color:#fff}
.util-register{left:592px;width:56px;background:var(--charcoal-2);color:#eee}
.util-shade{left:460px;top:0;width:64px;height:37px;background:#555}
.mainnav{left:0;top:37px;width:814px;height:20px;background:var(--slate)}
.navlink{top:42px;font-size:7.5px;color:#fff}
.phone{top:40px;left:558px;display:flex;align-items:center;gap:5px;color:#fff;font-size:7.5px;font-weight:700}
.phone-dot{width:13px;height:13px;border-radius:50%;background:var(--green);display:flex;align-items:center;justify-content:center}
.dropdown{left:358px;top:57px;width:92px;height:117px;background:var(--slate);z-index:3}
.dropdown a{display:block;height:16.4px;line-height:16px;padding-left:9px;font-size:7px;color:#fff;text-decoration:none;border-bottom:1px solid var(--slate-dark)}
/* hero */
.hero{left:0;top:57px;width:814px;height:199px;background:linear-gradient(90deg,#ececea 0%,#dcdad4 30%,#b7a58f 55%,#8a6d55 70%,#6d7e95 90%,#c7c5be 100%)}
.hero-title{left:198px;top:107px;font-family:Oswald,sans-serif;font-weight:600;font-size:23px;line-height:20.5px;color:#3e3e3e;letter-spacing:-.5px}
.hero-sub{left:199px;top:197px;font-size:11px;color:#3e3e3e;font-weight:300}
.search-tab{left:346px;top:230px;width:122px;height:26px;background:var(--green);color:#fff;font-size:9.5px;display:flex;align-items:center;justify-content:center;gap:4px}
.search-tab b{font-weight:700}
/* search panel */
.searchbox{left:170px;top:256px;width:477px;height:93px;background:linear-gradient(180deg,#5fd0ad,#3ebd96);box-shadow:0 6px 6px -3px rgba(0,0,0,.25)}
.searchbox::after{content:"";position:absolute;left:8px;right:8px;bottom:-5px;height:5px;background:var(--green-dark)}
.field{position:absolute;top:18px;width:81px}
.field label{display:block;font-size:7px;color:#2f6e5a;margin-bottom:3px}
.field span{display:block;height:18px;background:#fff}
.search-now{position:absolute;left:13px;top:54px;width:452px;height:24px;background:#eee;color:#555;font-size:9px;display:flex;align-items:center;justify-content:center;gap:4px}
/* ads */
.ad{background:linear-gradient(180deg,#e8e4e0 0%,#2a8ac8 30%,#1d72b2 85%,#fff 85%)}
.ad-left{left:170px;top:370px;width:49px;height:244px;border:1px solid #ccc}
.ad-right{left:598px;top:370px;width:49px;height:244px;background:linear-gradient(180deg,#0f2a55,#163a70 60%,#22324a)}
/* section titles */
.sec-title{font-size:10px;color:#3a3a3a;text-transform:uppercase}
.sec-title b{font-weight:700}
.sec-title span{font-weight:300}
.rule{height:1px;background:#d6d6d6}
/* categories */
.cat-panel{left:240px;top:402px;width:338px;height:212px;background:var(--green-pale)}
.cat{position:absolute;width:100px}
.cat-icon{position:absolute;left:-27px;top:-8px;width:18px;height:18px;border-radius:50%;background:var(--green);display:flex;align-items:center;justify-content:center}
.cat h4{font-size:7px;font-weight:700;color:#333;margin-bottom:4px}
.cat li{list-style:none;font-size:6.3px;color:#444;line-height:12px}
.btn-small{display:inline-flex;align-items:center;gap:3px;height:14px;padding:0 7px;background:#f4f4f4;font-size:5.3px;color:#444;text-transform:uppercase;box-shadow:1px 2px 0 #b8b8b8;margin-top:6px;margin-left:2px}
/* featured */
.band{left:0;top:652px;width:814px;height:150px;background:var(--grey-band)}
.job{position:absolute;top:661px;width:146px}
.job-tag{display:inline-block;background:var(--green);color:#fff;font-size:7px;padding:3px 4px}
.job-by{font-size:6.6px;color:var(--muted);margin:6px 0 0 4px}
.job-by b{color:var(--green);font-weight:700}
.job-cat{font-size:6.6px;color:#444;margin:3px 0 0 4px}
.job-cat b{font-weight:400;color:#222}
.job p{font-size:5.6px;line-height:8.5px;color:#666;margin:6px 0 0 4px}
.dots{left:388px;top:790px;display:flex;gap:4px}
.dots i{width:3px;height:3px;border-radius:50%;background:#333}
.dots i:first-child{background:var(--green)}
/* business solution */
.sol-photo{left:170px;top:834px;width:232px;height:156px;background:linear-gradient(135deg,#e8eef2,#c4ccd3 50%,#8b96a0)}
.sol-label{left:334px;top:976px;width:68px;height:14px;background:var(--green);color:#fff;font-size:6px;display:flex;align-items:center;justify-content:center}
.deal-title{left:170px;top:1000px;font-size:10px;color:#444;font-weight:300}
.deal-title b{font-weight:400;color:var(--green);font-size:7px}
.deal-text{left:170px;width:232px;font-size:5.7px;line-height:8.5px;color:#555}
.testi{left:415px;top:818px;width:399px;height:192px;background:var(--grey-panel)}
.avatar{left:494px;top:827px;width:74px;height:74px;border-radius:50%;background:linear-gradient(160deg,#eee,#c9b7a8 60%,#55606d);border:2px solid #fff}
.arrow{top:857px;width:16px;height:16px;border-radius:50%;background:var(--green-dark);display:flex;align-items:center;justify-content:center}
.t-name{left:415px;width:399px;top:907px;text-align:center;font-size:9px;font-weight:700;color:var(--green)}
.t-role{left:415px;width:399px;top:920px;text-align:center;font-size:6.5px;color:#444}
.t-box{left:422px;top:940px;width:220px;height:64px;background:#c6cad0;font-size:5.6px;line-height:8.3px;color:#555;text-align:center;padding:9px 14px}
.t-box::before{content:"";position:absolute;left:102px;top:-6px;border:6px solid transparent;border-top:0;border-bottom-color:#c6cad0}
.ad-bottom-a{left:422px;top:1018px;width:101px;height:100px;background:linear-gradient(180deg,#6f6d66,#3a3b3c 80%,#fff 80%)}
.ad-bottom-b{left:540px;top:1018px;width:102px;height:100px;background:linear-gradient(135deg,#f3d7dd,#d8a9b6 60%,#e0137c 85%)}
/* footer */
.footer{left:0;top:1134px;width:814px;height:36px;background:var(--charcoal)}
.f-brand{left:170px;top:1142px;font-weight:700;font-size:17px;color:#fff;display:flex;align-items:center;gap:4px}
.f-brand i{display:block;width:8px;height:8px;border-radius:50%;background:#fff}
.f-phone{left:288px;top:1145px;display:flex;align-items:center;gap:6px;color:#fff;font-size:7px}
.f-social-label{left:410px;top:1143px;color:#fff;text-align:right;line-height:8px}
.f-social-label small{display:block;font-size:5.5px}
.f-social-label b{font-size:9px;font-weight:400}
.socials{left:476px;top:1139px;display:flex;gap:5px}
.socials span{width:24px;height:24px;border-radius:5px;background:var(--green)}
.f-links{left:0;top:1170px;width:814px;height:14px;background:var(--green-dark);display:flex;justify-content:center;gap:13px;padding-left:6px;font-size:6px;color:#fff;align-items:center;text-transform:uppercase}
.f-copy{left:0;top:1184px;width:814px;height:16px;background:var(--green);font-size:5.5px;color:#fff;padding:5px 0 0 170px}
</style>
</head>
<body>

<!-- header -->
<div class="abs topbar"></div>
<div class="abs brand"></div>
<div class="abs brand-name"><i></i>TALVENTO</div>
<div class="abs util-shade"></div>
<div class="abs util-btn util-lang">
  <svg width="6" height="5" viewBox="0 0 6 5"><rect width="6" height="4" rx="1" fill="#666"/></svg>Language</div>
<div class="abs util-btn util-login">
  <svg width="6" height="6" viewBox="0 0 6 6"><path d="M1 0h5v6H1V4h1v1h3V1H2v1H1zM0 2.5h3V1.5l1.5 1.5L3 4.5V3.5H0z" fill="#fff"/></svg>Login</div>
<div class="abs util-btn util-register">
  <svg width="5" height="5" viewBox="0 0 5 5"><path d="M2 0h1v2h2v1H3v2H2V3H0V2h2z" fill="#ddd"/></svg>Register</div>

<nav class="abs mainnav"></nav>
<div class="abs navlink" style="left:170px">Company Searcher</div>
<div class="abs navlink" style="left:246px">Advises</div>
<div class="abs navlink" style="left:290px">Jobs</div>
<div class="abs navlink" style="left:327px">Solutions</div>
<div class="abs navlink" style="left:376px">About TALVENTO <span style="color:var(--green)">⌄</span></div>
<div class="abs phone"><span class="phone-dot"><svg width="7" height="7" viewBox="0 0 10 10"><path d="M2 0l2 2.5-1.2 1.2c.6 1.4 1.8 2.6 3.2 3.2L7.2 5.7 10 7.8 8.6 10C4 9.6.4 6 0 1.4z" fill="#fff"/></svg></span>Call us +00 555 010 200</div>

<div class="abs hero" role="img" aria-label="Photo of a smiling young man with glasses working at a laptop"></div>
<div class="abs dropdown">
  <a>About Us</a><a>Contact Us</a><a>Conditions</a><a>Site map</a><a>Community</a><a>Politics</a><a>Publicity</a>
</div>
<div class="abs hero-title">EASIAT WAY<br>TO FIND<br>YOUR<br>DREAM</div>
<div class="abs hero-sub">FIND A JOB</div>
<div class="abs search-tab"><svg width="7" height="7" viewBox="0 0 10 10"><circle cx="4" cy="4" r="3" fill="none" stroke="#fff" stroke-width="1.6"/><path d="M6 6l3.5 3.5" stroke="#fff" stroke-width="1.8"/></svg><b>COMPANIES</b> SEARCHER</div>

<!-- search -->
<div class="abs searchbox">
  <div class="field" style="left:14px"><label>Company Name</label><span></span></div>
  <div class="field" style="left:106px"><label>VAT Number</label><span></span></div>
  <div class="field" style="left:198px"><label>City / State</label><span></span></div>
  <div class="field" style="left:291px"><label>Zip / Postal Code</label><span></span></div>
  <div class="field" style="left:383px"><label>Country</label><span></span></div>
  <div class="search-now"><svg width="7" height="7" viewBox="0 0 10 10"><circle cx="4" cy="4" r="3" fill="none" stroke="#555" stroke-width="1.6"/><path d="M6 6l3.5 3.5" stroke="#555" stroke-width="1.8"/></svg>SEARCH NOW!</div>
</div>

<!-- ads -->
<div class="abs ad ad-left" role="img" aria-label="Vertical advertisement for online technology courses"></div>
<div class="abs ad-right" role="img" aria-label="Vertical advertisement for a smartphone"></div>

<!-- categories -->
<div class="abs sec-title" style="left:240px;top:380px"><b>Business</b> <span>Categories</span></div>
<div class="abs rule" style="left:240px;top:396px;width:338px"></div>
<div class="abs cat-panel"></div>

<div class="cat" style="left:277px;top:418px"><span class="cat-icon"><svg width="8" height="8" viewBox="0 0 8 8"><rect x=".5" y="1" width="7" height="6.5" fill="none" stroke="#fff"/><rect x="3" y="3.5" width="2" height="2" fill="#fff"/></svg></span>
  <h4>Entertainment</h4><ul><li>Theaters (5)</li><li>Bars (8)</li><li>Clubs (7)</li><li>Lounges (4)</li></ul><span class="btn-small">↳ View all</span></div>
<div class="cat" style="left:386px;top:418px"><span class="cat-icon"><svg width="8" height="8" viewBox="0 0 8 8"><circle cx="4" cy="4" r="3.3" fill="none" stroke="#fff"/><circle cx="4" cy="4" r="1.3" fill="#fff"/></svg></span>
  <h4>Parks &amp; Playgrounds</h4><ul><li>Amusement Parks (6)</li><li>Playgrounds (6)</li><li>Recreation Centers (6)</li><li>Sports Clubs (6)</li></ul><span class="btn-small">↳ View all</span></div>
<div class="cat" style="left:495px;top:418px"><span class="cat-icon"><svg width="8" height="8" viewBox="0 0 8 8"><rect x="1" y="2.5" width="6" height="5" fill="none" stroke="#fff"/><path d="M2.8 2.5V1.5a1.2 1.2 0 012.4 0v1" fill="none" stroke="#fff"/></svg></span>
  <h4>Shopping</h4><ul><li>Books &amp; Mags (7)</li><li>Fashion (7)</li><li>Jewellery (7)</li><li>Venues (6)</li></ul><span class="btn-small">↳ View all</span></div>

<div class="cat" style="left:277px;top:518px"><span class="cat-icon"><svg width="8" height="8" viewBox="0 0 8 8"><path d="M4 7.8L1.5 4.2A2.7 2.7 0 116.5 4.2z" fill="none" stroke="#fff"/><circle cx="4" cy="3" r="1" fill="#fff"/></svg></span>
  <h4>Places</h4><ul><li>Hotels (8)</li><li>Museums (5)</li><li>Parks (7)</li><li>Restaurants (7)</li></ul><span class="btn-small">↳ View all</span></div>
<div class="cat" style="left:386px;top:518px"><span class="cat-icon"><svg width="8" height="8" viewBox="0 0 8 8"><path d="M.5 4L4 .8 7.5 4M1.5 3.3V7.3h5V3.3" fill="none" stroke="#fff"/></svg></span>
  <h4>Real Estate</h4><ul><li>Apartments (6)</li><li>Commercial Places (5)</li><li>Residential Places (5)</li><li>Vacant Land (7)</li></ul><span class="btn-small">↳ View all</span></div>
<div class="cat" style="left:495px;top:518px"><span class="cat-icon"><svg width="8" height="8" viewBox="0 0 8 8"><circle cx="4" cy="4" r="1.7" fill="none" stroke="#fff"/><path d="M4 0v1.3M4 6.7V8M0 4h1.3M6.7 4H8M1.2 1.2l.9.9M5.9 5.9l.9.9M1.2 6.8l.9-.9M5.9 2.1l.9-.9" stroke="#fff" stroke-width=".8"/></svg></span>
  <h4>Vacation &amp; Holidays</h4><ul><li>Hostel (7)</li><li>Motel (7)</li><li>Appratments (7)</li><li>Venues (6)</li></ul><span class="btn-small">↳ View all</span></div>

<!-- featured job -->
<div class="abs sec-title" style="left:170px;top:631px"><b>Featured</b> <span>Job</span></div>
<div class="abs rule" style="left:170px;top:646px;width:477px"></div>
<div class="abs band"></div>

<div class="job" style="left:170px"><span class="job-tag">Content and Social Media Specialist</span>
  <div class="job-by">by <b>Company Name</b></div><div class="job-cat">Category: <b>Admin/Human Resources</b></div>
  <p>Consectetur adipisicing elit, sed do eiusmod tempor incididunt ut labore et dolore magna aliqua. Ut enim ad minim veniam, quis nostrud exercitation ullamco laboris nisi ut aliquip ex ea commodo consequat. Duis aute irure dolor in reprehenderit in voluptate velit esse cillum.</p>
  <span class="btn-small" style="margin-top:6px">▤ View details</span></div>
<div class="job" style="left:334px"><span class="job-tag">Technical Business Analyst/ Systems Analyst</span>
  <div class="job-by">by <b>Company Name</b></div><div class="job-cat">Category: <b>Admin/Human Resources</b></div>
  <p>Lorem ipsum dolor sit amet, consectetur adipisicing elit, sed do eiusmod tempor incididunt ut labore et dolore magna aliqua. Ut enim ad minim veniam, quis nostrud exercitation ullamco laboris nisi ut aliquip ex ea commodo consequat. Duis aute irure dolor in reprehenderit in voluptate velit esse cillum.</p>
  <span class="btn-small" style="margin-top:6px">▤ View details</span></div>
<div class="job" style="left:496px"><span class="job-tag">Web Analyst</span>
  <div class="job-by">by <b>Company Name</b></div><div class="job-cat">Category: <b>Admin/Human Resources</b></div>
  <p>Duis aute irure dolor in reprehenderit in voluptate velit esse cillum dolore eu fugiat nulla pariatur. Excepteur sint occaecat cupidatat non proident, sunt in culpa qui officia deserunt mollit anim id est laborum. Sed ut perspiciatis unde omnis iste natus error sit voluptatem accusantium.</p>
  <span class="btn-small" style="margin-top:6px">▤ View details</span></div>
<div class="abs dots"><i></i><i></i><i></i><i></i><i></i><i></i></div>

<!-- business solution -->
<div class="abs sec-title" style="left:171px;top:815px"><b>Business</b> <span>Solution</span></div>
<div class="abs rule" style="left:171px;top:830px;width:231px"></div>
<div class="abs sol-photo" role="img" aria-label="Photo of a businessman in a grey suit working at a computer by a window"></div>
<div class="abs sol-label">Business Real Estate</div>
<div class="abs deal-title">Business Deal <b>- by Company Name</b></div>
<p class="abs deal-text" style="top:1016px">Lorem ipsum dolor sit amet, consectetur adipisicing elit, sed do eiusmod tempor incididunt ut labore et dolore magna aliqua. Ut enim ad minim veniam, quis nostrud exercitation ullamco laboris nisi ut aliquip ex ea commodo consequat. Duis aute irure dolor in reprehenderit in voluptate velit esse cillum dolore eu fugiat nulla pariatur. Excepteur sint occaecat cupidatat non proident, sunt in culpa qui officia deserunt mollit anim id est laborum.</p>
<p class="abs deal-text" style="top:1068px">Sed ut perspiciatis unde omnis iste natus error sit voluptatem accusantium doloremque laudantium, totam rem aperiam, eaque ipsa quae ab illo inventore veritatis et quasi architecto beatae vitae dicta sunt explicabo. Nemo enim ipsam voluptatem quia voluptas sit aspernatur aut odit aut fugit, sed quia consequuntur magni dolores eos qui ratione voluptatem sequi nesciunt. Neque porro quisquam est, qui dolorem ipsum quia dolor sit amet, consectetur, adipisci velit, sed quia.</p>

<div class="abs testi"></div>
<div class="abs avatar" role="img" aria-label="Portrait photo of the reviewer"></div>
<div class="abs arrow" style="left:471px"><svg width="6" height="6" viewBox="0 0 6 6"><path d="M4 .5L1.5 3 4 5.5" fill="none" stroke="#fff" stroke-width="1.2"/></svg></div>
<div class="abs arrow" style="left:575px"><svg width="6" height="6" viewBox="0 0 6 6"><path d="M2 .5L4.5 3 2 5.5" fill="none" stroke="#fff" stroke-width="1.2"/></svg></div>
<div class="abs t-name">Marten Kole</div>
<div class="abs t-role">Webdesigner</div>
<div class="abs t-box">Lorem ipsum dolor sit amet, consectetur adipisicing elit, sed do eiusmod tempor incididunt ut labore et dolore magna aliqua. Ut enim ad minim veniam, quis nostrud exercitation ullamco laboris nisi ut aliquip ex ea commodo consequat. Duis aute irure dolor in reprehenderit in voluptate velit esse cillum dolore eu fugiat nulla pariatur. Excepteur sint occaecat cupidatat non proident, sunt in culpa qui officia deserunt mollit anim id est laborum.</div>
<div class="abs ad-bottom-a" role="img" aria-label="Advertisement for a programming bootcamp"></div>
<div class="abs ad-bottom-b" role="img" aria-label="Advertisement for beauty products"></div>

<!-- footer -->
<footer class="abs footer"></footer>
<div class="abs f-brand"><i></i>TALVENTO</div>
<div class="abs f-phone"><span class="phone-dot"><svg width="7" height="7" viewBox="0 0 10 10"><path d="M2 0l2 2.5-1.2 1.2c.6 1.4 1.8 2.6 3.2 3.2L7.2 5.7 10 7.8 8.6 10C4 9.6.4 6 0 1.4z" fill="#fff"/></svg></span>Call us +00 555 010 200</div>
<div class="abs f-social-label"><small>JOIN US ON</small><b>SOCIAL MEDIA</b></div>
<div class="abs socials">
  <span role="img" aria-label="Social network link"></span><span role="img" aria-label="Social network link"></span><span role="img" aria-label="Social network link"></span><span role="img" aria-label="Social network link"></span><span role="img" aria-label="Social network link"></span><span role="img" aria-label="Social network link"></span>
</div>
<div class="abs f-links"><span>About us</span><span>Contact us</span><span>Conditions</span><span>Site map</span><span>Community</span><span>Politics</span><span>Publicity</span></div>
<div class="abs f-copy">Copyright © 2015 by Talvento | All rights reserved</div>

</body>
</html>
```